Saltmarsh Courier Ad

I would Like to design a newspaper ad for a local paper I have attached a copy of what Ive used in the past as a jumping off point. Please be creative this is a high end location so please keep it elegant as well. the size needs to be 10" x 15.875"

I would like it to list services but not like it is right now, I don't need to have every specific thing that I do per service just an overview of what I actually do

Target Market(s)

Client clientele on Block island

Requirements
Must have
• I would like to see pictures as well as the list of services and any other suggestions you feel maybe important to have. Please utilize my website for ideas on what you can add to the ad. www.tidewellnb.com

```html
<!DOCTYPE html>
<html lang="en">
<head>
<meta charset="utf-8">
<title>Tidewell Pool Service – Saltmarsh Courier Ad</title>
<link href="https://fonts.googleapis.com/css2?family=Roboto+Condensed:wght@300;400;700&family=Open+Sans:wght@400;600&display=swap" rel="stylesheet">
<style>
  :root{
    --navy:#1c3a78;
    --navy-deep:#152d63;
    --orange:#f47a20;
    --orange-light:#f6a236;
    --page:#f3f4f5;
    --surround:#d3d5d8;
    --rule:#c9ccd0;
    --text:#3a3f47;
    --muted:#5d636c;
    --white:#ffffff;
  }
  *{margin:0;padding:0;box-sizing:border-box}
  html,body{width:880px;height:1200px;overflow:hidden;background:var(--surround)}
  .ad{position:absolute;left:62px;top:0;width:756px;height:1200px;overflow:hidden;background:var(--page);font-family:"Open Sans",sans-serif;color:var(--text)}
  .ad-art{position:absolute;inset:0}

  .brand{position:absolute;left:32px;top:52px;display:flex;align-items:center;gap:10px}
  .brand-mark{width:26px;height:26px;border-radius:50%;background:var(--orange)}
  .brand-name{font-family:"Roboto Condensed",sans-serif;font-weight:700;font-size:30px;color:var(--navy);letter-spacing:2px;line-height:1}
  .headline{position:absolute;right:30px;top:38px;text-align:right;font-family:"Roboto Condensed",sans-serif;line-height:1.08}
  .headline-top{display:block;font-size:32px;font-weight:300;color:var(--navy);letter-spacing:1px}
  .headline-main{display:block;font-size:40px;font-weight:700;color:var(--orange)}

  .benefits-title{position:absolute;left:30px;top:520px;font-family:"Roboto Condensed",sans-serif;font-weight:700;font-size:18px;line-height:1.3;color:var(--white);letter-spacing:.5px}

  .benefits{position:absolute;left:30px;top:632px;width:696px;display:grid;grid-template-columns:repeat(3,1fr);gap:26px}
  .benefit{position:relative;padding-left:16px;font-size:11.5px;line-height:1.5;color:var(--muted)}
  .benefit::before{content:"";position:absolute;left:0;top:4px;width:8px;height:8px;border-radius:50%;background:var(--orange)}

  .services-heading{position:absolute;left:30px;top:728px;width:696px;display:flex;align-items:center;gap:14px;font-family:"Roboto Condensed",sans-serif;font-weight:700;font-size:16px;letter-spacing:3px;color:var(--navy)}
  .services-heading::after{content:"";flex:1;height:1px;background:var(--rule)}
  .services{position:absolute;left:30px;top:766px;width:696px;display:grid;grid-template-columns:1fr 1fr;column-gap:40px;row-gap:18px;list-style:none}
  .service{border-left:3px solid var(--orange);padding-left:12px}
  .service-title{font-family:"Roboto Condensed",sans-serif;font-weight:700;font-size:14px;letter-spacing:.5px;color:var(--navy);margin-bottom:4px}
  .service-text{font-size:11.5px;line-height:1.5;color:var(--muted)}
  .service-wide{grid-column:1 / -1}

  .offer{position:absolute;left:30px;top:1112px;font-family:"Roboto Condensed",sans-serif;font-weight:700;font-size:18px;line-height:1.35;color:var(--white)}
  .offer span{color:var(--orange-light)}
  .social{position:absolute;left:300px;top:1140px;display:flex;gap:6px}
  .social i{display:block;width:15px;height:15px;background:var(--white);opacity:.85}
  .social i+i{background:var(--orange)}
  .contact{position:absolute;left:446px;top:1110px;font-family:"Roboto Condensed",sans-serif;font-weight:700;font-size:12.5px;line-height:1.35;color:var(--white)}
</style>
</head>
<body>
<main class="ad">
  <svg class="ad-art" width="756" height="1200" viewBox="0 0 756 1200">
    <defs>
      <linearGradient id="bg" x1="0" y1="0" x2="0" y2="1">
        <stop offset="0" stop-color="#f7f8f8"/><stop offset="0.5" stop-color="#e6e7e9"/><stop offset="1" stop-color="#f1f2f3"/>
      </linearGradient>
      <linearGradient id="orange" x1="0" y1="0" x2="1" y2="1">
        <stop offset="0" stop-color="#f6a236"/><stop offset="1" stop-color="#f06a1c"/>
      </linearGradient>
      <linearGradient id="garden" x1="0" y1="0" x2="0" y2="1">
        <stop offset="0" stop-color="#a3aca3"/><stop offset="0.55" stop-color="#5f6d4c"/><stop offset="1" stop-color="#b9d3d8"/>
      </linearGradient>
      <linearGradient id="pool" x1="0" y1="0" x2="0" y2="1">
        <stop offset="0" stop-color="#c9dbe6"/><stop offset="0.3" stop-color="#4d7a3e"/><stop offset="0.42" stop-color="#64b9c8"/><stop offset="1" stop-color="#2fa3bd"/>
      </linearGradient>
      <linearGradient id="person" x1="0" y1="0" x2="0" y2="1">
        <stop offset="0" stop-color="#c99a7a"/><stop offset="1" stop-color="#4c6f8c"/>
      </linearGradient>
    </defs>
    <rect width="756" height="1200" fill="url(#bg)"/>
    <rect width="756" height="150" fill="#ffffff" opacity=".6"/>
    <path d="M650 160 Q715 146 756 140 L756 500 Q745 300 650 160 Z" fill="url(#orange)"/>
    <path d="M0 400 Q160 478 390 488 L390 586 Q200 612 0 606 Z" fill="url(#orange)"/>
    <path d="M0 606 Q200 612 390 586 L390 597 Q200 623 0 617 Z" fill="#c6c8cb"/>
    <circle cx="160" cy="330" r="138" fill="url(#garden)" stroke="var(--navy)" stroke-width="7" role="img" aria-label="Photo of a garden hot tub beside a rustic stone and timber cottage"/>
    <circle cx="522" cy="380" r="212" fill="url(#pool)" stroke="var(--navy)" stroke-width="8" role="img" aria-label="Photo of a technician cleaning a large turquoise in-ground pool on a green lawn"/>
    <path d="M0 1044 Q260 1012 450 1082 Q492 1104 505 1200 L0 1200 Z" fill="var(--navy)"/>
    <path d="M348 1200 Q398 1060 536 1046 Q660 1036 756 1054 L756 1200 Z" fill="#ffffff"/>
    <path d="M360 1200 Q410 1070 540 1058 Q660 1048 756 1066 L756 1200 Z" fill="url(#orange)"/>
    <path d="M610 1200 L610 1040 Q650 990 690 992 Q738 996 750 1040 L750 1200 Z" fill="url(#person)" role="img" aria-label="Portrait of the pool service owner"/>
  </svg>

  <header>
    <div class="brand"><span class="brand-mark"></span><span class="brand-name">TIDEWELL</span></div>
    <h1 class="headline">
      <span class="headline-top">DIVE INTO PROFESSIONAL</span>
      <span class="headline-main">POOL SERVICE &amp; REPAIR</span>
    </h1>
  </header>

  <h2 class="benefits-title">THE BENEFITS OF CHOOSING<br>TIDEWELL POOL SERVICE</h2>

  <section class="benefits">
    <p class="benefit">Staff on island at least 3 days a week (April through October) with an island shop and vehicle.</p>
    <p class="benefit">Emergencies are handled quickly, and the difficult issues that arise are resolved with ease.</p>
    <p class="benefit">Trusted relationships with island pool builders for assistance on larger projects.</p>
  </section>

  <h2 class="services-heading">OUR SERVICES</h2>
  <ul class="services">
    <li class="service">
      <h3 class="service-title">POOL OPENING &amp; CLOSING</h3>
      <p class="service-text">Seasonal start-up and winterizing, handled completely.</p>
    </li>
    <li class="service">
      <h3 class="service-title">WEEKLY POOL SERVICE</h3>
      <p class="service-text">Balanced water and a clean pool, every week of summer.</p>
    </li>
    <li class="service">
      <h3 class="service-title">RENOVATION</h3>
      <p class="service-text">Tile, coping and plaster restored to a like-new finish.</p>
    </li>
    <li class="service">
      <h3 class="service-title">ELECTRONIC LEAK DETECTION</h3>
      <p class="service-text">State-of-the-art technology that finds leaks fast.</p>
    </li>
    <li class="service service-wide">
      <h3 class="service-title">EQUIPMENT REPAIR &amp; UPGRADES</h3>
      <p class="service-text">Service for all equipment, plus upgrades to quieter, more energy efficient systems.</p>
    </li>
  </ul>

  <footer>
    <p class="offer">WE OFFER FREE ESTIMATES AND<br><span>A SATISFACTION GUARANTEE!</span></p>
    <div class="social"><i></i><i></i></div>
    <p class="contact">SPECIALIZING IN<br>HIGH-END GUNITE POOLS<br>401-555-0147<br>www.tidewellnb.com</p>
  </footer>
</main>
</body>
</html>
```